Cedar Hall businesscard

We changed our name and logo, now we need new business cards.
3-4/72 Marlow Street Blacktown 2148
www.cedarhall-example.org.au
info@cedarhall-example.org.au
Lorna-Jean Whitcombe
Senior Pastor
ph: 02 95874210

```html
<!DOCTYPE html>
<html lang="en">
<head>
<meta charset="utf-8">
<title>Cedar Hall – Business Card</title>
<link rel="stylesheet" href="https://fonts.googleapis.com/css2?family=Exo+2:wght@300;800&family=Arimo:wght@400&display=swap">
<style>
  :root {
    --backdrop: #2e3538;
    --card: #ffffff;
    --panel-tint: #e1e6eb;
    --band: #97b8c4;
    --brand: #6685a2;
    --ink-light: #ffffff;
  }
  html, body {
    margin: 0;
    padding: 0;
    width: 1200px;
    height: 1000px;
    overflow: hidden;
    background: var(--backdrop);
  }
  .stage {
    position: relative;
    width: 1200px;
    height: 1000px;
  }
  .card-art {
    position: absolute;
    inset: 0;
  }
  .brand {
    position: absolute;
    left: 120px;
    top: 476px;
    width: 270px;
    display: flex;
    align-items: center;
    justify-content: center;
    gap: 12px;
  }
  .brand-dot {
    width: 20px;
    height: 20px;
    border-radius: 50%;
    background: var(--brand);
    flex: none;
  }
  .brand-name {
    margin: 0;
    font-family: "Exo 2", sans-serif;
    font-weight: 300;
    font-size: 36px;
    line-height: 42px;
    color: var(--brand);
    white-space: nowrap;
  }
  .person-name {
    position: absolute;
    left: 485px;
    top: 336px;
    margin: 0;
    font-family: "Exo 2", sans-serif;
    font-weight: 800;
    font-size: 41px;
    line-height: 48px;
    color: var(--ink-light);
    letter-spacing: 0.6px;
    white-space: nowrap;
  }
  .person-role {
    position: absolute;
    left: 485px;
    top: 382px;
    margin: 0;
    font-family: "Exo 2", sans-serif;
    font-weight: 300;
    font-size: 31px;
    line-height: 38px;
    color: var(--ink-light);
  }
  .contact-list {
    position: absolute;
    left: 485px;
    top: 530px;
    margin: 0;
    padding: 0;
    list-style: none;
    font-family: "Arimo", sans-serif;
    font-size: 21px;
    color: var(--ink-light);
  }
  .contact-item {
    display: flex;
    align-items: center;
    height: 28.5px;
    white-space: nowrap;
  }
  .contact-icon {
    width: 26px;
    height: 22px;
    margin-right: 19px;
    flex: none;
  }
</style>
</head>
<body>
<div class="stage">
  <svg class="card-art" width="1200" height="1000" viewBox="0 0 1200 1000" aria-hidden="true">
    <rect class="card" x="104" y="216" width="991" height="567" fill="var(--card)"/>
    <path class="side-panel" d="M104,216 L325,216 Q495,500 325,783 L104,783 Z" fill="var(--panel-tint)"/>
    <path class="info-band" d="M408,320 L1095,320 L1095,680 L408,680 Q466,500 408,320 Z" fill="var(--band)"/>
  </svg>

  <div class="brand">
    <span class="brand-dot"></span>
    <p class="brand-name">Cedar Hall</p>
  </div>

  <h1 class="person-name">Lorna-Jean Whitcombe</h1>
  <p class="person-role">Senior Pastor</p>

  <ul class="contact-list">
    <li class="contact-item">
      <svg class="contact-icon" viewBox="0 0 26 22" aria-hidden="true">
        <path d="M6,1 L10,1 L11,6 L8.5,8 Q11,13 15,16 L17,13.5 L22,15 L22,19 Q21,21 18,21 Q5,17 4,3 Q4,1 6,1 Z" fill="#fff"/>
      </svg>
      <span>02 95874210</span>
    </li>
    <li class="contact-item">
      <svg class="contact-icon" viewBox="0 0 26 22" aria-hidden="true">
        <rect x="1.5" y="4" width="23" height="15" fill="none" stroke="#fff" stroke-width="2"/>
        <path d="M1.5,4 L13,13 L24.5,4" fill="none" stroke="#fff" stroke-width="2"/>
      </svg>
      <span>info@cedarhall-example.org.au</span>
    </li>
    <li class="contact-item">
      <svg class="contact-icon" viewBox="0 0 26 22" aria-hidden="true">
        <path d="M12,1 Q5,1 5,8 Q5,12 12,21 Q19,12 19,8 Q19,1 12,1 Z" fill="#fff"/>
        <circle cx="12" cy="8" r="2.8" fill="var(--band)"/>
      </svg>
      <span>3-4/72 Marlow Street Blacktown 2148</span>
    </li>
    <li class="contact-item">
      <svg class="contact-icon" viewBox="0 0 26 22" aria-hidden="true">
        <circle cx="12" cy="11" r="9.5" fill="#fff"/>
        <path d="M6,6 Q9,8 8,11 Q11,12 10,16 M15,3 Q14,7 17,8 Q20,9 19,13" fill="none" stroke="var(--band)" stroke-width="1.6"/>
      </svg>
      <span>www.cedarhall-example.org.au</span>
    </li>
  </ul>
</div>
</body>
</html>
```